Ambervale Apple Moonshine Design

I would like to see if someone can take my design and make it awesome.This is a label for the front of the bottle the size of the label 3" x 5".

Target Market(s)

Alcohol & Spirits

Requirements
Must have
• Must have Photo with man, still and apple. All text must remain fonts can be changed.
Nice to have
• Wow factor

```html
<!DOCTYPE html>
<html lang="en">
<head>
<meta charset="utf-8">
<title>Ambervale Apple Shine Label</title>
<link rel="stylesheet" href="https://fonts.googleapis.com/css2?family=Sacramento&family=Chewy&family=Mulish:wght@500;600;800&display=block">
<style>
  :root {
    --sage: #879c59;
    --brick: #8a2620;
    --cream: #ebdfbb;
    --ink: #1d1c1e;
    --badge-red: #a8292a;
    --white: #ffffff;
  }
  html, body { margin: 0; padding: 0; overflow: hidden; }
  body { width: 720px; height: 1200px; }
  .label {
    position: relative;
    width: 720px;
    height: 1200px;
    background: var(--cream);
    overflow: hidden;
  }
  .header-band {
    position: absolute; left: 0; top: 0;
    width: 720px; height: 226px;
    background: var(--sage);
    text-align: center;
    color: var(--brick);
  }
  .edition {
    position: absolute; left: 0; right: 0; top: 46px;
    font-family: "Sacramento", cursive;
    font-size: 58px; line-height: 1;
  }
  .brand-name {
    position: absolute; left: 0; right: 0; top: 112px;
    font-family: "Mulish", sans-serif;
    font-weight: 800;
    font-size: 72px; line-height: 1;
    color: var(--brick);
  }
  .hero-figure {
    position: absolute; left: 250px; top: 292px;
    width: 330px; height: 634px;
    background: linear-gradient(180deg, #b98a6e 0%, #2e3650 18%, #3f5f8e 55%, #2a3f6e 100%);
    border-radius: 120px 120px 0 0;
  }
  .product-title {
    position: absolute; left: 0; top: 362px;
    width: 720px;
    text-align: center;
    font-family: "Chewy", cursive;
    font-size: 104px;
    line-height: 118px;
    color: var(--sage);
    -webkit-text-stroke: 14px var(--white);
    paint-order: stroke fill;
  }
  .footer-band {
    position: absolute; left: 0; top: 926px;
    width: 720px; height: 274px;
    background: var(--ink);
    color: var(--cream);
  }
  .proof-badge {
    position: absolute; left: 594px; top: 40px;
    width: 96px; height: 96px;
    border-radius: 50%;
    background: var(--badge-red);
    text-align: center;
    font-family: "Mulish", sans-serif;
    font-weight: 500;
    color: var(--cream);
  }
  .proof-number { display: block; font-size: 36px; line-height: 1; padding-top: 18px; }
  .proof-word { display: block; font-size: 16px; line-height: 1.2; }
  .abv {
    position: absolute; left: 592px; top: 140px; width: 100px;
    text-align: center;
    font-family: "Mulish", sans-serif; font-weight: 500; font-size: 20px;
  }
  .maker-line {
    position: absolute; left: 0; right: 0; top: 150px;
    text-align: center;
    font-family: "Mulish", sans-serif; font-weight: 500;
    font-size: 29px; letter-spacing: 1.5px;
  }
  .maker-name {
    position: absolute; left: 0; right: 0; top: 190px;
    text-align: center;
    font-family: "Mulish", sans-serif; font-weight: 600;
    font-size: 44px; line-height: 1.1;
  }
</style>
</head>
<body>
<div class="label">
  <header class="header-band">
    <div class="edition">Special Edition</div>
    <div class="brand-name">Tom Halden’s</div>
  </header>

  <div class="hero-figure" role="img" aria-label="Painted portrait of an old moonshiner in a hat and overalls holding a red apple beside a copper still"></div>

  <h1 class="product-title" style="margin:0">Ambervale<br>Apple<br>Shine</h1>

  <footer class="footer-band">
    <div class="proof-badge">
      <span class="proof-number">60</span>
      <span class="proof-word">Proof</span>
    </div>
    <div class="abv">30 ABV</div>
    <div class="maker-line">Distilled and Bottled by</div>
    <div class="maker-name">Ridgeline Distilling Co.</div>
  </footer>
</div>
</body>
</html>
```